Conservative, Modern and Sharp Builder Business card

Hi there,
We would like to update our existing business card.
I have attached photos of existing business card, logo and van sign.

I would like the business card to also list what we do :
Renovation • New Build • Alteration
Extension • Bathroom • Maintenance.(Seperated by dots)

Contact number : 021 0483 0752
(With that exact spacing)

Ideally when people looking from about 2-3 metres, they know that it is a builder’s business card

Open to suggestions on fonts, layout, style of business card

PLEASE ONLY SUBMIT YOUR BEST OR MAX 3 DESIGNS FOR EACH DESIGNER

Thanks

Industry/Entity Type

Construction. Renovation

Contact Information for Business Card

Details should be the same as the existing card. And addition of what we do.

Requirements
Should not have
• The new business card must not have the same layout as our existing one. Thanks

```html
<!DOCTYPE html>
<html lang="en">
<head>
<meta charset="utf-8">
<title>KeelstoneBuild Business Card</title>
<link href="https://fonts.googleapis.com/css2?family=Inter:wght@400;500;700&family=Source+Sans+3:wght@700&display=swap" rel="stylesheet">
<style>
  :root {
    --backdrop: #9b9b9b;
    --card-dark: #121212;
    --card-light: #ffffff;
    --ink: #111111;
    --ink-soft: #555555;
    --on-dark: #ececec;
  }
  * { margin: 0; padding: 0; box-sizing: border-box; }
  html, body { width: 1200px; height: 588px; overflow: hidden; }
  body { background: var(--backdrop); font-family: "Inter", sans-serif; position: relative; }

  .card { position: absolute; width: 487px; height: 287px; }
  .card-front { left: 87px; top: 141px; background: var(--card-dark); color: var(--on-dark); }
  .card-back { left: 622px; top: 143px; background: var(--card-light); color: var(--ink); }

  .front-brand {
    position: absolute; left: 0; right: 0; top: 100px;
    display: flex; justify-content: center; align-items: center; gap: 10px;
    font-family: "Source Sans 3", sans-serif; font-weight: 700; font-size: 40px;
    color: var(--on-dark); letter-spacing: 0.5px;
  }
  .brand-square { width: 14px; height: 14px; background: currentColor; flex: none; }

  .services {
    position: absolute; left: 0; right: 0; top: 229px;
    text-align: center; font-size: 13.5px; line-height: 19px;
    letter-spacing: 0.6px; color: var(--on-dark); font-weight: 400;
  }

  .back-brand {
    position: absolute; left: 21px; top: 82px;
    display: flex; align-items: center; gap: 8px;
    font-family: "Source Sans 3", sans-serif; font-weight: 700; font-size: 33px;
    color: var(--ink); letter-spacing: -0.3px;
  }
  .back-brand .brand-square { width: 11px; height: 11px; }

  .person { position: absolute; right: 19px; top: 131px; text-align: right; }
  .person-name { font-weight: 700; font-size: 18px; letter-spacing: 0.2px; line-height: 22px; }
  .person-role { font-size: 12.5px; color: var(--ink-soft); line-height: 18px; }

  .divider { position: absolute; left: 22px; right: 19px; top: 178px; height: 1px; background: var(--ink); }

  .contacts { position: absolute; left: 21px; top: 192px; list-style: none; }
  .contacts li { display: flex; align-items: center; gap: 7px; height: 19.7px; font-size: 13.5px; color: #444; }
  .contacts li.phone { font-weight: 700; font-size: 14.5px; color: var(--ink); }
  .contacts svg { width: 11px; height: 11px; flex: none; fill: var(--ink); }
</style>
</head>
<body>
  <section class="card card-front">
    <div class="front-brand"><span class="brand-square"></span>KeelstoneBuild</div>
    <p class="services">RENOVATION • NEW BUILD • ALTERATION<br>EXTENSION • BATHROOM • MAINTENANCE</p>
  </section>

  <section class="card card-back">
    <div class="back-brand"><span class="brand-square"></span>KeelstoneBuild</div>
    <div class="person">
      <p class="person-name">MARLO TENNANT</p>
      <p class="person-role">Residential Builder</p>
    </div>
    <div class="divider"></div>
    <ul class="contacts">
      <li class="phone">
        <svg viewBox="0 0 24 24" aria-hidden="true"><path d="M6.6 10.8a15.1 15.1 0 0 0 6.6 6.6l2.2-2.2c.3-.3.7-.4 1-.2 1.1.4 2.3.6 3.6.6.6 0 1 .4 1 1V20c0 .6-.4 1-1 1C10.6 21 3 13.4 3 4c0-.6.4-1 1-1h3.5c.6 0 1 .4 1 1 0 1.3.2 2.5.6 3.6.1.3 0 .7-.2 1z"/></svg>
        021 0483 0752
      </li>
      <li>
        <svg viewBox="0 0 24 24" aria-hidden="true"><path d="M2 5h20v14H2z" fill="none"/><path d="M2 5h20v2l-10 6L2 7zM2 9l10 6 10-6v10H2z"/></svg>
        KeelstoneBuild@mailbox.com
      </li>
      <li>
        <svg viewBox="0 0 24 24" aria-hidden="true"><circle cx="12" cy="12" r="10"/><path d="M2 12h20M12 2c3 3 3 17 0 20M12 2c-3 3-3 17 0 20" stroke="#fff" stroke-width="1.6" fill="none"/></svg>
        www.KeelstoneBuild.com
      </li>
      <li>
        <svg viewBox="0 0 24 24" aria-hidden="true"><circle cx="12" cy="12" r="9" fill="none" stroke="#111" stroke-width="2.5"/></svg>
        KeelstoneBuild.nz
      </li>
    </ul>
  </section>
</body>
</html>
```